Residential Mortgage Leader needs Wordpress Design

Looking for a home page website design for a client. We develop using the WordPress platform and would prefer the design be at least loosely based on an existing WordPress template. Attached files have many notes from our creative brief with client. The site must be responsive. Approved, basic wireframe attached. There is room for interpretation.

Existing web site: http://www.marisolvantreek.example/

The Marisol Vantreek Team relies on strong systems to deliver an on-time, done-right, friendly experience. Marisol offers mortgages and refinancing services throughout the United States. She is a successful Keystone Loanworks agent who strives to be an active part of her community. She would like to focus the site on her team, rather than just her.

Difference makers...
When you work with the Marisol Vantreek team you get a high level of expertise and a friendly experience.

She has amazing credentials. Marisol is widely recognized as a top producer for her company, and has earned a number of awards and honors for her customer service.

Marisol's team is very engaged and enjoys sharing social comments or photos from their community.

Imagery:
* Friendly, warm imagery, preferably of her team or an image to represent her team
* Clean and crisp
* Professional / Experts in mortgage and refinance
* Clean / Good use of white space
Updates

When possible, please use imagery from the DFW area. The client mentioned they would prefer not to see stock images. Thanks.

Amend that- creative use of stock images, however, is fine. A few designs have used stock imagery, but in a well-considered manner.

We added some photos and graphics that are local. We are Dallas / Ft. Worth, Plano, Frisco, Texas. We also added some examples of photos to use for the "In the Community" area. Stock photos of business folks just doesn't fit there. Thanks!

Target Market(s)

They service a lot of builders, but also work with homeowners. Their typical client is usually a woman searching for mortgage services online. She typically has a family and may refer her husband to Marisol's team. Keep in mind, however, they also see a number of other scenarios. Most of their clients are middle to high-end borrowers.

Industry/Entity Type

It Company

Requirements
Must have
• Design should be developed using program such as Photoshop or Fireworks or Illustrator as last preference. Ideally, the design would be based on an existing responsive WordPress theme, which we would customize. You must include the name of the target theme. The footer should include lots of space for disclaimers and legal language. Site navigation should include these choices: "Home, About, Builders, Mortgage Info, Approval, Blog, Contact"
Nice to have
• Blog, social media and photos area. Use of the already approved style prototype with colors and fonts (Lato- a Google font, Times New Roman and Cookie-a decorative Google font). However, we are open to interpretation.
Should not have
• Hard to read fonts or a lack of white space.

```html
<!DOCTYPE html>
<html lang="en">
<head>
<meta charset="utf-8">
<title>Keystone Loanworks – Marisol Vantreek Team</title>
<link rel="stylesheet" href="https://fonts.googleapis.com/css2?family=Lato:ital,wght@0,300;0,400;0,700;0,900;1,400&display=swap">
<style>
:root{
  --dark:#262626;
  --darker:#161616;
  --footer:#2b2b2b;
  --red:#b5160f;
  --red-light:#e0402c;
  --card:#f6f6f6;
  --text:#8c8c8c;
  --heading:#2a2a2a;
  --line:#e3e3e3;
  --white:#ffffff;
  --foot-text:#c9c9c9;
  --foot-muted:#8e8e8e;
}
*{margin:0;padding:0;box-sizing:border-box}
html,body{width:1001px;height:1200px;overflow:hidden}
body{font-family:'Lato',sans-serif;background:var(--white);position:relative;color:var(--text)}
.abs{position:absolute}

.header-band{left:0;top:0;width:1001px;height:422px;background:var(--dark);border-top:4px solid #3a3a3a}
.call-box{left:744px;top:4px;width:167px;height:28px;background:#3b3b3b;color:#fff;font-size:13.5px;display:flex;align-items:center;padding-left:8px;gap:6px;white-space:nowrap}
.call-box b{font-weight:700}
.brand{left:110px;top:42px;color:#fff;font-size:29px;font-weight:700;letter-spacing:-.3px;display:flex;align-items:center;gap:10px}
.brand-dot{width:18px;height:18px;background:#fff;border-radius:50%}
.brand-sub{left:110px;top:73px;color:#fff;font-size:13.5px;font-weight:400}
.nav{left:454px;top:58px;display:flex;align-items:center}
.nav a{color:#e6e6e6;font-size:11.5px;text-decoration:none;padding:4px 11px}
.nav a.active{background:var(--red);color:#fff;font-weight:700;font-size:12.5px;padding:5px 8px;margin-right:3px}

.hero{left:108px;top:114px;width:802px;height:348px;background:linear-gradient(90deg,#f8efe2 0%,#eedcc4 35%,#e7c9a4 55%,#f3e4cf 75%,#fbf5ec 100%)}
.hero-shadow{left:125px;top:462px;width:780px;height:40px;background:radial-gradient(ellipse at 50% 0%,rgba(0,0,0,.55) 0%,rgba(0,0,0,.15) 55%,rgba(0,0,0,0) 75%)}
.caption{left:85px;top:207px;width:304px;height:147px;background:var(--darker);padding:14px 0 0 30px;color:#fff}
.caption-fold{left:85px;top:354px}
.caption h1{font-weight:400;font-size:26px;letter-spacing:-.3px}
.caption p{font-size:11px;line-height:16px;margin-top:12px;width:270px}
.caption .actions{display:flex;align-items:center;gap:8px;margin-top:17px;font-size:11px}
.btn-red{background:var(--red);color:#fff;padding:7px 14px;font-size:10.5px}
.btn-white{background:#fff;color:#222;padding:7px 11px;font-size:10.5px}

.card{top:548px;width:236px;height:140px;background:var(--card);text-align:center;padding-top:34px;z-index:1}
.card h2{font-size:14.5px;font-weight:400;color:var(--heading);letter-spacing:.2px}
.card p{font-size:10.6px;line-height:13.6px;margin:8px 14px 0}
.card .more{color:var(--red);font-size:10px;margin-top:9px;display:block}
.icon{width:38px;height:38px;border-radius:50%;background:var(--red);top:530px;display:flex;align-items:center;justify-content:center;z-index:2}

.divider{left:125px;top:714px;width:776px;height:1px;background:var(--line)}
.side{left:125px;top:736px;width:216px}
.side-item{height:38px;border-bottom:1px solid var(--line);border-right:1px solid var(--line);display:flex;align-items:center;gap:9px;font-size:12.5px;color:var(--heading)}
.side-item.first{border-right:none;height:34px}
.dot{width:25px;height:25px;border-radius:50%;background:#e8e8e8}
.dot.red{background:var(--red)}
.community{left:374px;top:740px;width:522px}
.community h2{font-size:14px;font-weight:700;color:#3a3a3a;letter-spacing:.2px}
.community p{font-size:11px;line-height:15px;margin-top:12px}

.footer{left:0;top:914px;width:1001px;height:242px;background:var(--footer)}
.footer-rule{left:110px;top:958px;width:795px;height:1px;background:#454545}
.foot-h{top:932px;color:#fff;font-size:13px}
.foot-p{font-size:10.7px;line-height:15.3px;color:var(--foot-text)}
.foot-p .hl{color:var(--red-light)}
.btn-contact{left:111px;top:1071px;background:var(--red);color:#fff;font-size:11px;padding:6px 11px}
.select{left:384px;top:1067px;width:186px;height:27px;background:#5b5b5b;color:#ddd;font-style:italic;font-size:11px;display:flex;align-items:center;justify-content:space-between;padding:0 9px}
.portrait{left:633px;top:982px;width:98px;height:106px;border:2px solid #555;background:linear-gradient(160deg,#5c4636,#a77e62 55%,#2b2420)}
.manager{left:752px;top:981px;color:#fff;font-size:13.5px;font-weight:300}
.details{left:752px;top:1014px;width:150px;font-size:11px;line-height:17px;color:var(--foot-muted);white-space:nowrap}
.bottom-bar{left:0;top:1156px;width:1001px;height:44px;background:var(--darker)}
.legal{left:109px;top:1171px;font-size:11px;color:#8a8a8a}
.housing-badge{left:875px;top:1163px;width:28px;height:28px;background:#e5e5e5}
</style>
</head>
<body>

<div class="abs header-band"></div>
<div class="abs call-box">
  <svg width="9" height="14" viewBox="0 0 9 14"><rect x="0.5" y="0.5" width="8" height="13" rx="1.5" fill="none" stroke="#fff"/><circle cx="4.5" cy="11" r="0.9" fill="#fff"/></svg>
  <b>Call Us:</b> <span>555-014-7890</span>
</div>
<div class="abs brand"><span>Keystone Loanworks</span><span class="brand-dot"></span></div>
<div class="abs brand-sub">A Ridgeline Capital Company</div>
<nav class="abs nav">
  <a class="active">HOME</a><a>About Us</a><a>Builders</a><a>Mortage Info</a><a>Approval</a><a>Blog</a><a>Contact Us</a>
</nav>

<div class="abs hero-shadow"></div>
<div class="abs hero" role="img" aria-label="Photo of a smiling couple toasting with champagne beside a sold sign in a bright new home"></div>
<div class="abs caption">
  <h1>Earning Your Business</h1>
  <p>The Marisol Vantreek Team relies on strong systems to deliver on-time, done-right and friendly experience</p>
  <div class="actions"><span class="btn-red">Start Here</span><span>Or</span><span class="btn-white">Get to know us</span></div>
</div>
<svg class="abs caption-fold" width="24" height="16"><polygon points="0,0 24,0 24,16" fill="#111"/></svg>

<div class="abs card" style="left:125px">
  <h2>OUR CREDENTIALS</h2>
  <p>Lorem Ipsum is simply dummy text of the printing and typesetting industry. Lorem Ipsum has been the industry's standard dummy text ever since the 1500s</p>
  <span class="more">[ Read More . . . ]</span>
</div>
<div class="abs card" style="left:392px">
  <h2>AWARDS</h2>
  <p>Lorem Ipsum is simply dummy text of the printing and typesetting industry. Lorem Ipsum has been the industry's standard dummy text ever since the 1500s</p>
  <span class="more">[ Read More . . . ]</span>
</div>
<div class="abs card" style="left:660px">
  <h2>RECOGNITION</h2>
  <p>Lorem Ipsum is simply dummy text of the printing and typesetting industry. Lorem Ipsum has been the industry's standard dummy text ever since the 1500s</p>
  <span class="more">[ Read More . . . ]</span>
</div>

<div class="abs icon" style="left:224px">
  <svg width="18" height="18" viewBox="0 0 18 18"><path d="M3 9.5l4 4 8-9" fill="none" stroke="#fff" stroke-width="2.2"/></svg>
</div>
<div class="abs icon" style="left:491px">
  <svg width="18" height="18" viewBox="0 0 18 18"><path d="M5 2h8v5a4 4 0 0 1-8 0z M9 11v3 M6 16h6" fill="none" stroke="#fff" stroke-width="1.6"/></svg>
</div>
<div class="abs icon" style="left:759px">
  <svg width="16" height="18" viewBox="0 0 16 18"><rect x="2" y="1" width="12" height="16" fill="none" stroke="#fff" stroke-width="1.6"/><circle cx="8" cy="10" r="2.4" fill="none" stroke="#fff" stroke-width="1.4"/><path d="M5 5h6" stroke="#fff" stroke-width="1.4"/></svg>
</div>

<div class="abs divider"></div>
<div class="abs side">
  <div class="side-item first"><span class="dot red"></span>Engaged in our Community</div>
  <div class="side-item"><span class="dot"></span>Blog</div>
  <div class="side-item"><span class="dot"></span>Social</div>
  <div class="side-item"><span class="dot"></span>In the Community</div>
</div>
<div class="abs community">
  <h2>ENGAGED IN OUR COMMUNITY</h2>
  <p>Lorem Ipsum is simply dummy text of the printing and typesetting industry. Lorem Ipsum has been the industry's standard dummy text ever since the 1500s, when an unknown printer took a galley of type and scrambled it to make a type specimen book. It has survived not only five centuries, but also the leap into electronic typesetting, remaining essentially unchanged. It was popularised in the 1960s with the release of Letraset sheets containing Lorem Ipsum passages, and more recently with desktop publishing software like Aldus PageMaker including versions of Lorem Ipsum.</p>
</div>

<footer>
  <div class="abs footer"></div>
  <div class="abs footer-rule"></div>
  <div class="abs foot-h" style="left:112px">Disclaimer</div>
  <div class="abs foot-h" style="left:386px">Language</div>
  <div class="abs foot-h" style="left:636px">About Marisol Vantreek</div>
  <p class="abs foot-p" style="left:112px;top:978px;width:225px"><span class="hl">Lorem Ipsum</span> is simply dummy text of the printing and typesetting industry. Lorem Ipsum has been the industry's standard dummy text ever since the 1500s, when an unknown printer took a galley of type and scrambled</p>
  <div class="abs btn-contact">Be contacted by a customer consultant</div>
  <p class="abs foot-p" style="left:384px;top:977px;width:200px">Lorem Ipsum is simply dummy text of the printing and typesetting industry. Lorem Ipsum has been the industry's standard dummy text ever since the 1500s</p>
  <div class="abs select"><span>English</span><svg width="9" height="7"><polygon points="0,0 9,0 4.5,7" fill="#ccc"/></svg></div>
  <div class="abs portrait" role="img" aria-label="Portrait photo of the branch manager"></div>
  <div class="abs manager">Branch Manager</div>
  <div class="abs details">Office: 555.014.2200<br>Cell: 555.014.8830<br>mvantreek@kloanworks.example<br>NMLS: 40917<br>4820 Cedar Row, Ste.210<br>Maple Bend, TX 75990<br>Directions</div>
  <div class="abs bottom-bar"></div>
  <div class="abs legal">Marisol Vantreek • Legal</div>
  <div class="abs housing-badge" role="img" aria-label="Housing opportunity badge"></div>
</footer>

</body>
</html>
```